We need a refreshed business card. Our company is a venture capital investment firm focused on investing in medical devices. Logo is attached. please also see our website www.velmoracapital.example

Target Market(s)

investors and potential investment targets

Industry/Entity Type

medical investments

Contact Information for Business Card

logo, name, title, email, phone, website, address,

Colors
0054AA
0677BA
7BADD7
CADEEF
E8F1F8
0094D4
00A9DD
6FCCEA
C7EBF8
E9F6FB
00AB8E
00BBA5
67D7C9
C6EFE9
E9F9F6

Requirements
Must have
• fresh modern design
Nice to have
• QR code leading to our linked in page, short description of what we do “Early Stage Medical Device Investors”

```html
<!DOCTYPE html>
<html lang="en">
<head>
<meta charset="utf-8">
<title>Velmora Capital Partners – Business Card</title>
<link href="https://fonts.googleapis.com/css2?family=Lato:ital,wght@0,400;0,700;1,400&display=swap" rel="stylesheet">
<style>
  :root {
    --blue-deep: #0054AA;
    --blue-mid: #0677BA;
    --teal: #00AB8E;
    --teal-light: #00BBA5;
    --white: #FFFFFF;
    --ink: #1F2A33;
    --backdrop: #E6E6E6;
  }
  * { margin: 0; padding: 0; box-sizing: border-box; }
  html, body {
    width: 1200px; height: 1200px; overflow: hidden;
    background: var(--backdrop);
    font-family: "Lato", sans-serif;
  }
  .canvas { position: relative; width: 1200px; height: 1200px; }

  .card {
    position: absolute; left: 262px; width: 686px; height: 392px;
    border-radius: 20px; overflow: hidden;
    box-shadow: 0 18px 30px rgba(0,0,0,0.18);
  }
  .card--front { top: 165px; background: var(--white); }
  .card--back {
    top: 653px;
    background: linear-gradient(180deg, var(--teal-light) 0%, var(--teal) 100%);
  }
  .card__shapes { position: absolute; inset: 0; }

  .brand {
    position: absolute; left: 0; width: 380px; top: 150px;
    text-align: center; color: var(--blue-deep);
  }
  .brand__name {
    display: inline-flex; align-items: center; gap: 10px;
    font-size: 58px; font-weight: 700; line-height: 1;
  }
  .brand__dot {
    width: 14px; height: 14px; border-radius: 50%; background: var(--teal);
  }
  .brand__tagline {
    margin-top: 14px; font-size: 14px; color: var(--ink); letter-spacing: 0.3px;
  }

  .contact {
    position: absolute; left: 410px; top: 108px; color: var(--white);
  }
  .contact__name { font-size: 23px; font-weight: 700; line-height: 1.1; }
  .contact__title { font-size: 16px; font-style: italic; margin-top: 2px; }
  .contact__address { margin-top: 16px; font-size: 16px; line-height: 19px; }
  .contact__list { list-style: none; margin-top: 14px; font-size: 16px; line-height: 19px; }
  .contact__list li { display: flex; align-items: center; gap: 8px; }
  .contact__icon { width: 13px; height: 13px; flex: none; }

  .back__brand {
    position: absolute; left: 0; right: 0; top: 110px;
    display: flex; justify-content: center; align-items: center; gap: 16px;
    color: var(--white); font-size: 108px; font-weight: 700; line-height: 1;
  }
  .back__dot { width: 26px; height: 26px; border-radius: 50%; background: var(--white); }
  .back__web {
    position: absolute; left: 0; right: 0; top: 334px; text-align: center;
    color: var(--white); font-size: 15px; letter-spacing: 7px;
  }
</style>
</head>
<body>
<div class="canvas">

  <section class="card card--front">
    <svg class="card__shapes" viewBox="0 0 686 392" width="686" height="392" aria-hidden="true">
      <defs>
        <linearGradient id="panelBlue" x1="0" y1="0" x2="0" y2="1">
          <stop offset="0" stop-color="#0E6AB2"/>
          <stop offset="1" stop-color="#0754A6"/>
        </linearGradient>
      </defs>
      <polygon points="0,52 37,392 0,392" fill="var(--teal)"/>
      <polygon points="333,0 686,0 686,392 375,392" fill="url(#panelBlue)"/>
    </svg>

    <div class="brand">
      <div class="brand__name"><span class="brand__dot"></span>Velmora</div>
      <div class="brand__tagline">VELMORA CAPITAL PARTNERS</div>
    </div>

    <div class="contact">
      <div class="contact__name">Daniel Marsh, CFA</div>
      <div class="contact__title">CEO</div>
      <div class="contact__address">
        2270 Fernbrook Ave.<br>Suite 410<br>Austin, TX 78701
      </div>
      <ul class="contact__list">
        <li>
          <svg class="contact__icon" viewBox="0 0 16 16" aria-hidden="true"><path fill="#fff" d="M3.6 1.2l2.3 2.5-1.3 1.8c.9 2 2.4 3.5 4.4 4.4l1.8-1.3 2.5 2.3-1.4 2.6C7.2 13.2 2.8 8.8 1 3z"/></svg>
          555-014-2280
        </li>
        <li>
          <svg class="contact__icon" viewBox="0 0 16 16" aria-hidden="true"><rect x="1" y="3.5" width="14" height="9" rx="1" fill="#fff"/><path d="M1.5 4.5l6.5 4.5 6.5-4.5" stroke="#0A5DAB" stroke-width="1.3" fill="none"/></svg>
          info@velmoracapital.example
        </li>
        <li>
          <svg class="contact__icon" viewBox="0 0 16 16" aria-hidden="true"><circle cx="8" cy="8" r="7" fill="#fff"/><ellipse cx="8" cy="8" rx="3" ry="7" fill="none" stroke="#0A5DAB" stroke-width="1.2"/><line x1="1" y1="8" x2="15" y2="8" stroke="#0A5DAB" stroke-width="1.2"/></svg>
          velmoracapital.example
        </li>
      </ul>
    </div>
  </section>

  <section class="card card--back">
    <div class="back__brand"><span class="back__dot"></span>Velmora</div>
    <div class="back__web">WWW.VELMORACAPITAL.EXAMPLE</div>
  </section>

</div>
</body>
</html>
```